Poster Design for Film: 'Tres Lunas'

Tres Lunas means "two times" in Spanish. This short film is based on the true story of Cuban refugee during the take over of the Varela regime in 1959 and how is experiences and stories affected his children and grandchildren. Tres Lunas tells the story of Gabriel- a recent grad who is forced to choose between his critically ill grandfather, the business opportunity of a lifetime, and maintaining a relationship with his love interest, Veronica. Through his grandfather's recollections as a young man in 1950's Cuba, Gabriel gains a new outlook on life and the things that matter most.

This poster should evoke the drama and truth that the film approaches in a cinematic manner while maintaining the influences of true Cuban culture and history as perceived by a Miami audience today.

For more information please take a look at our fund raising site:
http://www.fundmorrow.example/projects/tres-lunas

The grandfather's current life (the Cuban revolutionary/refugee as an old man):
www.clipvault.example/48215907
password: treslunas

A quick teaser of the film, exploring the lives of Gabriel (the protagonist; grandson to Cuban refugee/revolutionary) and Vero (Gabriel's love interest he neglects to commit to):

http://www.streamtube.example/watch?v=QbRk7wPxNaT

Please let me know if you would like any stills of the film, have any questions, etc. Thanks!
Updates

Hey all! So sorry for the delay on the stills- we had some serious technical issues, but now they are up!

Please let me know if you have any questions. We'll be uploaded more stills to choose from tonight.

Thanks!

Hey all!
Unless you need something in specific, I have just uploaded the final stills for the poster. Feel free to use any of the images, but please keep in mind that the main characters are Gabe (the grandson), and his grandfather Ernesto both young and old. In other words- the three guys.

Please let me know if you have any questions. Thanks! 

Here are some small text details for the bottom of the poster:

A Copper Lantern Production in association with BrightWharf Studios and the Coastal Bay University. Starring Owen Castell, Marisol Quiroga, Tariq Bustamante, Lucia Ortega, Halim Sabbagh. Written, Directed, & Produced by Rafael Ostrova. Director of Photography Tomas Urbina. Edited by Rafael Ostrova & Tomas Urbina.

Hey designers!

I've just uploaded a new still of the main character. Please try to include it in your design, as it is preferred over the other stills of the main character.

Thanks!

I've just uploaded two small logos to be featured on the bottom of the poster.

Thanks!

Target Market(s)

Hollywood. Cuban-Americans. Miamians. Film Critics. Students. Professors.

Adults based in Los Angeles and Miami aged 21-50 that speak English and Spanish and are in the art and entertainment industry.

Industry/Entity Type

Business

Requirements
Must have
• Must evoke the style of Cuba in the late 1950's while staying true to current day culture/style for 20-somethings in America (specifically LA, NYC, Miami).
Nice to have
• A sort of serious, almost stoic style that could possibly evoke a melancholic reaction.
Should not have
• Anything that evokes a daytime soap opera.

```html
<!DOCTYPE html>
<html lang="en">
<head>
<meta charset="utf-8">
<title>Tres Lunas — Film Poster</title>
<link rel="stylesheet" href="https://fonts.googleapis.com/css2?family=Bebas+Neue&display=swap">
<style>
  :root {
    --paper: #efede8;
    --poster-red: #ec1c24;
    --shadow-dark: 20, 4, 6;
    --type-white: #ffffff;
  }
  html, body {
    margin: 0;
    padding: 0;
    width: 800px;
    height: 1200px;
    overflow: hidden;
    background: var(--paper);
  }
  .poster {
    position: relative;
    width: 800px;
    height: 1200px;
    background: var(--paper);
    font-family: "Bebas Neue", "Arial Narrow", sans-serif;
    color: var(--type-white);
  }
  .poster__field {
    position: absolute;
    left: 30px;
    top: 32px;
    width: 733px;
    height: 1134px;
    background: var(--poster-red);
    overflow: hidden;
  }
  .poster__figure {
    position: absolute;
    left: 95px;
    top: 40px;
    width: 500px;
    height: 1000px;
    background:
      radial-gradient(ellipse 38% 30% at 48% 78%, rgba(var(--shadow-dark), .9) 0 45%, rgba(var(--shadow-dark), 0) 100%),
      radial-gradient(ellipse 42% 48% at 55% 42%, rgba(var(--shadow-dark), .92) 0 60%, rgba(var(--shadow-dark), 0) 100%);
  }
  .poster__title {
    position: absolute;
    right: 379px; /* right edge at x = 384 on canvas */
    top: 450px;
    margin: 0;
    font-weight: 400;
    font-size: 172px;
    line-height: 134px;
    text-align: right;
    letter-spacing: 1px;
  }
  .poster__title span { display: block; }
  .poster__director {
    position: absolute;
    left: 380px;
    top: 628px;
    line-height: 1;
  }
  .poster__director-label {
    display: block;
    font-size: 23px;
    letter-spacing: .5px;
  }
  .poster__director-name {
    display: block;
    font-size: 52px;
    margin-top: 2px;
  }
  .poster__cast {
    position: absolute;
    right: 379px;
    top: 738px;
    margin: 0;
    padding: 0;
    list-style: none;
    text-align: right;
    font-size: 32px;
    line-height: 34px;
  }
  .poster__billing {
    position: absolute;
    left: 0;
    right: 0;
    top: 1076px;
    text-align: center;
    font-size: 13px;
    line-height: 18px;
    letter-spacing: .2px;
  }
  .poster__billing p { margin: 0; }
  .billing__label {
    display: inline-block;
    font-size: 6px;
    line-height: 6px;
    vertical-align: middle;
    text-align: left;
    margin: 0 3px;
  }
</style>
</head>
<body>
  <div class="poster">
    <div class="poster__field">
      <div class="poster__figure" role="img" aria-label="Dark silhouette of an older man in profile, head bowed, dissolving into smoke at the bottom"></div>

      <h1 class="poster__title"><span>TRES</span><span>LUNAS</span></h1>

      <div class="poster__director">
        <span class="poster__director-label">DIRECTED BY</span>
        <span class="poster__director-name">RAFAEL OSTROVA</span>
      </div>

      <ul class="poster__cast">
        <li>HALIM SABBAGH</li>
        <li>MARISOL QUIROGA</li>
        <li>TARIQ BUSTAMANTE</li>
        <li>OWEN CASTELL</li>
        <li>LUCIA ORTEGA</li>
      </ul>

      <div class="poster__billing">
        <p><span class="billing__label">A</span>COPPER LANTERN<span class="billing__label">PRODUCTION</span><span class="billing__label">IN ASSOCIATION<br>WITH</span>BRIGHTWHARF STUDIOS <span class="billing__label">AND</span>THE COASTAL BAY UNIVERSITY. <span class="billing__label">STARRING</span>OWEN CASTELL, MARISOL QUIROGA, TARIQ BUSTAMANTE, LUCIA ORTEGA, HALIM SABBAGH.</p>
        <p><span class="billing__label">WRITTEN AND<br>DIRECTED BY</span>RAFAEL OSTROVA. <span class="billing__label">DIRECTOR OF<br>PHOTOGRAPHY</span>TOMAS URBINA. <span class="billing__label">EDITED<br>BY</span>RAFAEL OSTROVA &amp; TOMAS URBINA.</p>
      </div>
    </div>
  </div>
</body>
</html>
```